Manufacturer Website with Home and Product page

We have this website, velamora.com, but we need another one for the Canadian market. Canadians like to deal with Canadians so we need to gear it to that. It will be a simpler website than the current site.

We will need a design for two pages, one for the home page and one for a product page.

I synthesized all the brief information for the designers here, descriptions for both pages are included:

https://files.quentrix.net/doc/8hQz3LmPw2RkTn5VbYc7XsJd4FgAe6UoNi0KtE/view?ref=share

Supporting Folder:
https://store.quentrix.net/store/folders/7bozN2MdWqJrTpC4XaLyVk?ref=share
Updates

Need extra days to review

Industry/Entity Type

Tanning Beds, Red Light Beds, Hydro massage beds

Number of Pages Required

2 page

Requirements
Must have
• Two page descriptions: https://files.quentrix.net/doc/8hQz3LmPw2RkTn5VbYc7XsJd4FgAe6UoNi0KtE/view
Nice to have
• Information Folder: https://store.quentrix.net/store/u/0/folders/7bozN2MdWqJrTpC4XaLyVk

```html
<!DOCTYPE html>
<html lang="en">
<head>
<meta charset="UTF-8">
<title>Velamora Canada – Home</title>
<link href="https://fonts.googleapis.com/css2?family=Jost:wght@300;400;500;600;700&display=swap" rel="stylesheet">
<style>
  :root {
    --page-bg: #f7f7f9;
    --ink: #1c1c24;
    --brand-blue: #5a6fc8;
    --accent-red: #ee1c1c;
    --hero-light: #c3cbef;
    --hero-mid: #9aa9e3;
    --hero-deep: #6f86d4;
    --white: #ffffff;
    --dot-ring: #ee1c1c;
  }
  * { margin: 0; padding: 0; box-sizing: border-box; }
  html, body {
    width: 1200px; height: 1000px; overflow: hidden;
    background: var(--page-bg);
    font-family: "Jost", sans-serif;
    color: var(--ink);
  }
  .site { position: relative; width: 1200px; height: 1000px; }

  /* Header */
  .site-header { position: absolute; left: 0; top: 0; width: 1200px; height: 70px; }
  .brand {
    position: absolute; left: 61px; top: 14px;
    font-size: 34px; font-weight: 500; color: var(--brand-blue); letter-spacing: -0.5px;
  }
  .main-nav { position: absolute; top: 24px; left: 0; }
  .nav-item {
    position: absolute; white-space: nowrap;
    font-size: 12.5px; font-weight: 500; color: var(--ink);
    display: flex; align-items: center; gap: 3px;
  }
  .nav-item svg { width: 9px; height: 9px; }
  .nav-item.is-active::after {
    content: ""; position: absolute; left: 50%; top: 21px;
    width: 4px; height: 4px; margin-left: -2px; border-radius: 50%;
    background: var(--accent-red);
  }
  .header-phone {
    position: absolute; left: 900px; top: 24px;
    display: flex; align-items: center; gap: 7px;
    font-size: 12.5px; font-weight: 600;
  }
  .header-phone svg { width: 15px; height: 15px; }
  .catalog-button {
    position: absolute; left: 1013px; top: 19px; width: 137px; height: 28px;
    background: var(--accent-red); color: var(--white); border-radius: 5px;
    font-size: 12.5px; font-weight: 500;
    display: flex; align-items: center; justify-content: center;
  }

  /* Hero */
  .hero {
    position: absolute; left: 16px; top: 70px; width: 1168px; height: 446px;
    border-radius: 10px; overflow: hidden;
    background: radial-gradient(ellipse 60% 70% at 55% 20%, #e4e7f8 0%, rgba(228,231,248,0) 70%),
                linear-gradient(180deg, var(--hero-light) 0%, var(--hero-mid) 55%, var(--hero-deep) 100%);
  }
  .hero-copy { position: absolute; left: 42px; top: 122px; color: var(--white); }
  .hero-kicker { font-size: 26px; font-weight: 300; letter-spacing: 0.3px; line-height: 1; }
  .hero-title {
    margin-top: 12px; font-size: 33px; font-weight: 600; line-height: 42px;
    letter-spacing: 0.2px; text-transform: uppercase;
  }
  .hero-title .light { font-weight: 300; }
  .hero-button {
    display: inline-flex; align-items: center; justify-content: center;
    margin-top: 14px; width: 126px; height: 26px;
    background: var(--accent-red); color: var(--white); border-radius: 5px;
    font-size: 11.5px; font-weight: 500;
  }
  .slide-counter { position: absolute; left: 42px; top: 372px; color: var(--white); font-size: 11px; }
  .slide-counter .current { position: absolute; left: 0; top: 0; }
  .slide-counter .track {
    position: absolute; left: 0; top: 24px; width: 102px; height: 1px;
    background: rgba(255,255,255,0.45);
  }
  .slide-counter .track::before {
    content: ""; position: absolute; left: 0; top: 0; width: 20px; height: 1px; background: var(--white);
  }
  .slide-counter .total { position: absolute; left: 60px; top: 34px; }
  .product-lineup {
    position: absolute; left: 501px; top: 88px; width: 372px; height: 256px;
    border-radius: 14px;
    background: linear-gradient(160deg, #f2f2f6 0%, #d9c9e9 40%, #e6c39a 65%, #f4f4f7 100%);
  }
  .model-portrait {
    position: absolute; left: 948px; top: 0; width: 220px; height: 446px;
    background: linear-gradient(180deg, #e9c4b5 0%, #e2a98d 50%, #f0b07a 100%);
    border-radius: 120px 0 0 0;
  }

  /* Slider dots */
  .slider-dots { position: absolute; left: 574px; top: 531px; display: flex; gap: 6px; }
  .slider-dots span {
    width: 7px; height: 7px; border-radius: 50%; border: 1px solid var(--dot-ring);
  }
  .slider-dots span.is-active { background: var(--accent-red); }

  /* Featured */
  .featured-title {
    position: absolute; left: 0; top: 564px; width: 1200px; text-align: center;
    font-size: 28px; font-weight: 600; color: var(--brand-blue); letter-spacing: 0.3px;
  }
  .product-card {
    position: absolute; top: 623px; width: 327px; height: 377px;
    border-radius: 8px 8px 0 0; overflow: hidden;
    box-shadow: 0 6px 18px rgba(60,70,120,0.12);
  }
  .card-tanning { left: 53px; background: linear-gradient(180deg, #f3b8e6 0%, #d8a2e0 60%, #c9b3ee 100%); }
  .card-massage { left: 442px; background: linear-gradient(180deg, #6e6a7c 0%, #b39a7a 45%, #a09ad0 100%); }
  .card-redlight { left: 831px; background: linear-gradient(180deg, #f24a2a 0%, #f0a0c8 55%, #e6d2ee 100%); }
</style>
</head>
<body>
<div class="site">
  <header class="site-header">
    <div class="brand">Velamora</div>
    <nav class="main-nav">
      <span class="nav-item is-active" style="left:293px">Home</span>
      <span class="nav-item" style="left:356px">Tanning <svg viewBox="0 0 10 10"><path d="M2 3.5 L5 6.5 L8 3.5" fill="none" stroke="#ee1c1c" stroke-width="1.6"/></svg></span>
      <span class="nav-item" style="left:434px">Massage <svg viewBox="0 0 10 10"><path d="M2 3.5 L5 6.5 L8 3.5" fill="none" stroke="#ee1c1c" stroke-width="1.6"/></svg></span>
      <span class="nav-item" style="left:517px">Red Light <svg viewBox="0 0 10 10"><path d="M2 3.5 L5 6.5 L8 3.5" fill="none" stroke="#ee1c1c" stroke-width="1.6"/></svg></span>
      <span class="nav-item" style="left:603px">Salon Startup</span>
      <span class="nav-item" style="left:697px">About Us</span>
      <span class="nav-item" style="left:770px">Contact Us</span>
    </nav>
    <div class="header-phone">
      <svg viewBox="0 0 24 24"><path d="M6.6 3.5 L9.5 3 L11 7.5 L8.8 9.2 C9.9 11.6 12.4 14.1 14.8 15.2 L16.5 13 L21 14.5 L20.5 17.4 C20.3 18.6 19.2 19.5 18 19.4 C10.6 18.8 5.2 13.4 4.6 6 C4.5 4.8 5.4 3.7 6.6 3.5 Z" fill="none" stroke="#ee1c1c" stroke-width="1.6" stroke-linejoin="round"/><path d="M14 4 A6 6 0 0 1 20 10 M14 7 A3 3 0 0 1 17 10" fill="none" stroke="#ee1c1c" stroke-width="1.4" stroke-linecap="round"/></svg>
      416.555.0172
    </div>
    <a class="catalog-button">Request a Catalog</a>
  </header>

  <section class="hero">
    <div class="hero-copy">
      <div class="hero-kicker">THE LEADING MANUFACTURER IN</div>
      <h1 class="hero-title">Commercial Tanning,<br>Red Light <span class="light">and</span><br>Water Massage Therapy</h1>
      <a class="hero-button">View Our Products</a>
    </div>
    <div class="slide-counter">
      <span class="current">01</span>
      <span class="track"></span>
      <span class="total">05</span>
    </div>
    <div class="product-lineup" role="img" aria-label="Product lineup: tanning bed, stand-up tanning booth, red light panel and water massage bed"></div>
    <div class="model-portrait" role="img" aria-label="Portrait of a woman in profile with glowing skin"></div>
  </section>

  <div class="slider-dots">
    <span class="is-active"></span><span></span><span></span><span></span><span></span>
  </div>

  <h2 class="featured-title">OUR FEATURED PRODUCTS</h2>
  <div class="product-card card-tanning" role="img" aria-label="Featured tanning bed with pink lamps"></div>
  <div class="product-card card-massage" role="img" aria-label="Featured salon room with water massage bed"></div>
  <div class="product-card card-redlight" role="img" aria-label="Featured red light therapy bed"></div>
</div>
</body>
</html>
```